Scent Marketing Solutions by Vapolinth

We need to create 12 page brochure (including the cover and back page) for our Scent Marketing line of products.

The brochure size is 18 cm x 18 cm.

Our competitors are www.breeze-olfa.example and www.nosquell.example
Updates

Hi Designers, 

The budget for this project has been increased to $300. This is a 12 page brochure of size 18cm x 18cm.

Thank you.

Hi all designers,

I uploaded a new brochure draft with the write up in pdf.
I understand that some of you could not open the original file in powerpoint.

Thank you.

Hi Designers,

I added the brochure write up in Word and PDF format. I understand some of you have troubles with it in the earlier files uploaded.

Thank you.

Target Market(s)

B2B audience, such as visual merchandisers of retail brands, hotel managers, real estate property managers etc.

Industry/Entity Type

Marketing

Requirements
Must have
• Our corporate identity uses a lot of white, hence this must be reflected in the brochure.
Our products are high-tech and environmentally friendly, so this must again be reflected in the design.
We want to make the brochure attractive and easy to read, hence would like to allocate more space for photos and pictures and keep the brochure as spacious as possible.
Nice to have
• Since the product is related to the air (it scents the air), we would like to have a design feature that reflects this and is repeated throughout the brochure. It can be a pattern or logo.
Should not have
• Avoid using a lot of bright colors

```html
<!DOCTYPE html>
<html lang="en">
<head>
<meta charset="utf-8">
<title>Vapolinth – The right scent changes everything</title>
<link href="https://fonts.googleapis.com/css2?family=Jost:ital,wght@0,300;0,400;1,400&display=swap" rel="stylesheet">
<style>
  :root {
    --paper: #ffffff;
    --ink: #1d1d1b;
    --sky: #5aaee3;
    --air-tint: rgba(143, 191, 230, 0.30);
    --air-fade: rgba(143, 191, 230, 0);
    --photo-top: #d4e3f2;
    --photo-mid: #86a06c;
    --photo-low: #c9d2dc;
    --photo-base: #eef2f6;
    --folio: #555555;
  }
  * { margin: 0; padding: 0; box-sizing: border-box; }
  html, body { width: 1200px; height: 600px; overflow: hidden; background: var(--paper); }
  .spread {
    position: relative;
    width: 1200px;
    height: 600px;
    overflow: hidden;
    background: var(--paper);
    font-family: "Jost", "Century Gothic", sans-serif;
    color: var(--ink);
  }
  .feature-photo {
    position: absolute;
    left: 33px; top: 33px;
    width: 533px; height: 533px;
    background:
      radial-gradient(circle at 22% 70%, rgba(255,255,255,0.75), rgba(255,255,255,0) 30%),
      radial-gradient(circle at 55% 72%, rgba(240,244,248,0.8), rgba(255,255,255,0) 32%),
      linear-gradient(180deg, var(--photo-top) 0%, var(--photo-mid) 38%, var(--photo-low) 68%, var(--photo-base) 100%);
  }
  .air-motif {
    position: absolute;
    left: 566px; top: 430px;
    width: 634px; height: 170px;
    background:
      radial-gradient(ellipse 60% 70% at 80% 75%, var(--air-tint), var(--air-fade) 100%),
      radial-gradient(ellipse 45% 50% at 30% 90%, rgba(143,191,230,0.18), var(--air-fade) 100%);
  }
  .headline {
    position: absolute;
    left: 630px; top: 66px;
    font-weight: 300;
    font-size: 44px;
    line-height: 53px;
    color: var(--sky);
    letter-spacing: 0.4px;
    white-space: nowrap;
  }
  .copy-column {
    position: absolute;
    top: 188px;
    font-size: 13.6px;
    line-height: 16.9px;
    font-weight: 400;
    white-space: nowrap;
  }
  .copy-intro { left: 632px; }
  .copy-range { left: 821px; }
  .copy-kit { left: 1009px; }
  .scent-list { list-style: none; margin: 16.9px 0; }
  .scent-list li { position: relative; padding-left: 13px; }
  .scent-list li::before {
    content: "";
    position: absolute;
    left: 1px; top: 6px;
    width: 5px; height: 5px;
    border-radius: 50%;
    background: var(--sky);
  }
  .more { font-style: italic; }
  .folio {
    position: absolute;
    left: 33px; top: 570px;
    font-size: 10px;
    font-style: italic;
    color: var(--folio);
  }
</style>
</head>
<body>
<div class="spread">
  <div class="feature-photo" role="img" aria-label="Silver Christmas baubles with swirl patterns among pine branches on a pale blue sparkling background"></div>

  <div class="air-motif" role="img" aria-label="Soft flowing airy line pattern in pale blue"></div>

  <h1 class="headline">The right scent<br>changes everything</h1>

  <div class="copy-column copy-intro">
    <p>With our extensive<br>library of more than<br>1,000 different scents<br>and our capabilities to<br>design signature scents<br>exclusively for your<br>brand, finding the right<br>scent for your business is<br>easy. The right scent can<br>draw customers into your<br>premises, make them<br>stay longer, and create a<br>subconscious bond that<br>makes customers think<br>of you every time they<br>experience your unique<br>scent.</p>
  </div>

  <div class="copy-column copy-range">
    <p>Vapolinth has<br>all types of scents,<br>including:</p>
    <ul class="scent-list">
      <li>Signature scents</li>
      <li>Mood influencing<br>scents (e.g. calming,<br>uplifting etc)</li>
      <li>Festive scents (e.g.<br>Christmas, New Year,<br>etc.)</li>
      <li>Themed scents (e.g.<br>beach, garden, etc.)</li>
      <li>Product scents (e.g.<br>coffee, popcorn etc.)</li>
    </ul>
    <p class="more">And so much more…</p>
  </div>

  <div class="copy-column copy-kit">
    <p>Enclosed in this kit is a<br>series of scents our Scent<br>Experts have handpicked<br>for your business.<br>We will be glad to meet<br>up with your team to<br>understand more about<br>your needs and to select<br>or design an exclusive<br>scent for you.</p>
  </div>

  <div class="folio">3 &amp; 4</div>
</div>
</body>
</html>
```